Tolvern Business Cards

Business card design. dont mind if new logo is suggested.
it would be for a security company.
our clients would be bigger security companies around Australia.
have a logo done but can be replaced. see attaached. like the colors.
Need company name, person name, designation, phone and email on front.
At back company logo and name. website saddress and 2 x license numbers
would like to have 2 different background color for both sidde

Industry/Entity Type

Security

Contact Information for Business Card

round corners, front should be light in color. need logo at back with webaddress and 2 x license numners

Font styles to use
Sans Serif

Colors
f37122
faa54b
f8ba93
0255a3
0592cd
85cae6
b3d448
9bcb3c
ffffff

Requirements
Must have
• see description
Nice to have
• see description
Should not have
• should not be difficult to read or hardd to find information on card.. lets say easy on eyes yet catchy

```html
<!DOCTYPE html>
<html lang="en">
<head>
<meta charset="utf-8">
<title>Tolvern Security Group – Business Cards</title>
<link rel="stylesheet" href="https://fonts.googleapis.com/css2?family=Jost:wght@300;400&family=Tinos:wght@700&display=swap">
<style>
  :root {
    --stage: #15191c;
    --lime: #a6fd29;
    --paper: #ffffff;
    --brand-blue: #1a4fe0;
    --sky: #3ab6f0;
    --label: #f2f2f2;
  }
  * { box-sizing: border-box; margin: 0; padding: 0; }
  html, body { width: 1200px; height: 1200px; overflow: hidden; background: var(--stage); }
  .stage { position: relative; width: 1200px; height: 1200px; font-family: "Jost", sans-serif; }

  .side-label {
    position: absolute; left: 0; width: 1200px; text-align: center;
    color: var(--label); font-family: "Jost", sans-serif; font-weight: 300;
    font-size: 26px; font-variant: small-caps; letter-spacing: 1px;
  }
  .side-label--back { top: 30px; }
  .side-label--front { top: 1136px; }

  .card {
    position: absolute; left: 172px; width: 856px; height: 522px;
    border-radius: 8px; overflow: hidden;
  }
  .card--back { top: 72px; background: var(--lime); color: var(--paper); }
  .card--front { top: 606px; background: var(--paper); color: var(--brand-blue); }

  .brand-dot { position: absolute; left: 50%; border-radius: 50%; transform: translateX(-50%); }
  .card--back .brand-dot { top: 115px; width: 190px; height: 190px; background: var(--paper); }
  .card--front .brand-dot { top: 52px; width: 122px; height: 122px; background: var(--sky); }

  .company-name {
    position: absolute; left: 0; width: 100%; text-align: center;
    font-family: "Tinos", serif; font-weight: 700; text-transform: uppercase; white-space: nowrap;
  }
  .card--back .company-name { top: 312px; font-size: 45px; letter-spacing: 0.5px; }
  .card--front .company-name { top: 175px; font-size: 27px; letter-spacing: 0.3px; }

  .person { position: absolute; left: 0; width: 100%; text-align: center; }
  .person__name { position: absolute; top: 264px; left: 0; width: 100%; font-size: 35px; font-weight: 400; letter-spacing: 1.5px; }
  .person__role { position: absolute; top: 317px; left: 0; width: 100%; font-size: 15px; font-weight: 400; letter-spacing: 0.5px; }

  .contact-row { position: absolute; left: 0; top: 456px; width: 100%; height: 40px; font-weight: 300; font-size: 23px; white-space: nowrap; }
  .contact-row span { position: absolute; top: 6px; }
  .contact-row .address { left: 52px; }
  .contact-row .email { left: 357px; top: 2px; }
  .contact-row .phone { left: 678px; }
  .contact-row .divider { position: absolute; top: 2px; width: 1px; height: 32px; background: currentColor; }
  .contact-row .divider--one { left: 330px; }
  .contact-row .divider--two { left: 652px; }
  .card--back .contact-row { opacity: 0.95; }
</style>
</head>
<body>
<div class="stage">
  <div class="side-label side-label--back">Back View</div>

  <section class="card card--back">
    <div class="brand-dot"></div>
    <div class="company-name">Tolvern Security Group</div>
    <div class="contact-row">
      <span class="address">14 kelton street NSW 2618</span>
      <i class="divider divider--one"></i>
      <span class="email">dara@tolvernsecurity.com.au</span>
      <i class="divider divider--two"></i>
      <span class="phone">0452 318 207</span>
    </div>
  </section>

  <section class="card card--front">
    <div class="brand-dot"></div>
    <div class="company-name">Tolvern Security Group</div>
    <div class="person">
      <div class="person__name">LOREM IPSUM</div>
      <div class="person__role">DIRECTOR</div>
    </div>
    <div class="contact-row">
      <span class="address">14 kelton street NSW 2618</span>
      <i class="divider divider--one"></i>
      <span class="email">dara@tolvernsecurity.com.au</span>
      <i class="divider divider--two"></i>
      <span class="phone">0452 318 207</span>
    </div>
  </section>

  <div class="side-label side-label--front">Front Look</div>
</div>
</body>
</html>
```